Parcelnook.com.au Front page Re-Design

We need a front page redesign for the website parcelnook.com.au,
The site needs to keep a number of products products highlighted on the front page. Same buttons but navigation could be different and we still need some text for SEO.
What we do not currently like:
1. The big banners.
2. The use of too much orange especially the 50% orange borders.
3. the fact that products cannot be seen straight away when logged-in.
4. The fact that it is hard to convert to tablet friendly
5. The fact that it's not a modern design.

What we think we want:

1. Maybe more use of 1 colour (purple or orange) with the other a secondary highlight colour.
2. A more modern look
3. The wow factor

Look at parcelnook.com.au take the elements that you need and design.
Updates

Reason: Designs are getting better. liking the designs that don't look like the usual e-commerce templates out there.

Hello,

We are making decisions next Monday. Sorry for the delay but there has been a lot of holidays in Australia and decision makers away.

Industry/Entity Type

Seo

Colors
6b449b
f78f20
ffffff

```html
<!DOCTYPE html>
<html lang="en">
<head>
<meta charset="utf-8">
<title>Parcelnook.com.au – Gift Baskets &amp; Hampers</title>
<link href="https://fonts.googleapis.com/css2?family=Open+Sans:ital,wght@0,400;0,600;0,700;1,400&family=Oswald:wght@500;600&display=swap" rel="stylesheet">
<style>
:root{
  --purple:#6b449b;
  --purple-dark:#553481;
  --orange:#f78f20;
  --white:#ffffff;
  --ink:#333333;
  --muted:#777777;
  --line:#e0e0e0;
  --header-bg:#ececec;
}
*{box-sizing:border-box;margin:0;padding:0}
html,body{width:1200px;height:2655px;overflow:hidden}
body{position:relative;background:var(--white);font-family:"Open Sans",Arial,sans-serif;color:var(--ink)}
.abs{position:absolute}

.site-header{left:0;top:0;width:1200px;height:133px;background:var(--header-bg);border-top:6px solid var(--purple)}
.brand{left:133px;top:38px;display:flex;align-items:center;gap:10px}
.brand-mark{width:26px;height:26px;background:var(--orange)}
.brand-name{font-weight:700;font-size:25px;color:var(--purple)}
.phone{left:578px;top:14px;display:flex;align-items:center;gap:8px;color:var(--purple);font-size:19px;font-weight:600}
.account-tab{left:773px;top:0;width:285px;height:42px;background:var(--purple);border-radius:0 0 10px 10px;color:var(--white);font-size:12px;font-weight:600;display:flex;align-items:center;justify-content:center;gap:6px}
.search{left:584px;top:77px;width:474px;height:36px;background:var(--white);border:1px solid #d6d6d6;display:flex;align-items:center;justify-content:space-between;padding:0 10px;font-size:11px;font-style:italic;color:#999}

.main-nav{left:0;top:136px;width:1200px;height:48px;background:linear-gradient(#fff,#f3f3f3);border-bottom:1px solid #e4e4e4}
.main-nav ul{position:absolute;left:133px;top:6px;width:930px;height:36px;list-style:none;display:flex;justify-content:space-between;align-items:center}
.main-nav li{font-size:13px;font-weight:600;color:var(--purple);padding:0 9px;height:36px;line-height:36px;border-right:1px solid #ddd}
.main-nav li:last-child{border-right:0}
.main-nav li.active{background:var(--orange);color:var(--white)}

.hero{left:131px;top:196px;width:648px;height:330px;border:2px solid var(--purple);background:linear-gradient(180deg,#eef4fb 0%,#d8e6f5 55%,#c9dcf0 100%);overflow:hidden}
.hero-photo{position:absolute;border-radius:50%;box-shadow:0 4px 10px rgba(0,0,0,.2)}
.hero-photo.big{left:11px;top:23px;width:262px;height:262px;background:radial-gradient(circle at 50% 45%,#e23b3b 0%,#f0a72b 25%,#3a7bd5 40%,#e6e6e6 55%,#cfcfcf 100%)}
.hero-photo.small{left:240px;top:150px;width:130px;height:130px;background:radial-gradient(circle at 50% 45%,#d8432f 0%,#f4b235 25%,#4c8a3a 42%,#e6e6e6 56%,#cfcfcf 100%)}
.hero-title{position:absolute;right:14px;top:20px;text-align:right}
.hero-title .deal{font-family:"Oswald",sans-serif;font-weight:600;font-size:50px;line-height:1;color:var(--purple)}
.hero-title .product{font-size:19px;font-weight:600;color:#222;margin-top:6px}
.hero-note{position:absolute;right:18px;top:194px;text-align:right;font-size:18px;font-weight:600;color:#222;line-height:1.35}
.hero-tabs{position:absolute;left:0;bottom:0;width:100%;height:48px;display:flex}
.hero-tabs div{flex:1;background:var(--purple);color:var(--white);text-align:center;font-size:11px;line-height:1.35;padding-top:8px;text-transform:uppercase}
.hero-tabs div small{display:block;text-transform:none;font-size:10px}
.hero-tabs div.current{background:var(--white);color:#333;border-bottom:4px solid var(--orange)}

.promo-exclusive{left:788px;top:196px;width:281px;height:330px}
.promo-card{position:absolute;left:0;width:281px}
.promo-card.orange{top:0;height:166px;background:var(--orange);color:var(--white);text-align:center;padding-top:8px}
.promo-card.grey{top:172px;height:158px;background:#d9d9d9;border:2px solid #c9c9c9;text-align:center;padding-top:6px}
.promo-card h3{font-size:19px;font-weight:600}
.promo-card p{font-size:12px;line-height:1.35;margin-top:2px}
.promo-label{position:absolute;left:62px;top:84px;width:158px;height:60px;background:var(--white);display:flex;align-items:center;justify-content:center;gap:6px}
.promo-label span:last-child{font-size:14px;font-weight:700;color:var(--purple)}
.promo-label .mark{width:12px;height:12px;background:var(--orange)}
.promo-round{position:absolute;left:84px;top:38px;width:112px;height:112px;border-radius:50%;background:radial-gradient(circle,#8b5a1f 0%,#c9a34f 35%,#f3f3f3 60%,#e6e6e6 100%)}
.shop-now{position:absolute;right:0;bottom:0;background:#555;color:var(--white);font-size:11px;padding:4px 10px}
.promo-card.grey .shop-now{background:none;color:#333}

.intro{left:140px;top:548px;width:920px;text-align:center}
.intro h1{font-size:22px;font-weight:400;color:var(--purple)}
.intro .lead{font-size:12.5px;font-weight:700;margin-top:8px;color:#222}
.intro p{font-size:12px;line-height:1.5;margin-top:3px}

.side-box{left:133px;width:228px;background:var(--white);border:1px solid var(--line);padding:4px}
.side-box h4{background:var(--purple);color:var(--white);font-size:14px;font-weight:600;height:32px;line-height:32px;padding-left:10px;margin-bottom:4px}
.side-box li{list-style:none;font-size:11.5px;height:30px;line-height:30px;border-bottom:1px solid #ececec;padding-left:12px;display:flex;align-items:center;gap:10px}
.side-box li:last-child{border-bottom:0}
.bullet{width:9px;height:9px;background:var(--orange);transform:rotate(45deg);flex:none}
.side-ad{left:133px;width:228px}
.ad-floral{top:1496px;height:120px;background:linear-gradient(90deg,#ece7f4 0%,#f0e9f2 60%,#f6e0ec 100%);border:1px solid #ddd}
.ad-floral .text{position:absolute;left:12px;top:8px;color:var(--purple);font-size:24px;line-height:1.15}
.ad-floral .text b{font-size:27px}
.ad-floral .flowers{position:absolute;right:8px;top:10px;width:105px;height:78px;border-radius:40%;background:radial-gradient(circle,#f27db0 0%,#f4a9c9 40%,#cfe3b3 80%,transparent 100%)}
.ad-floral .caption{position:absolute;right:10px;bottom:10px;font-size:12px;font-weight:700;font-style:italic;color:#e0338c}
.ad-secure{top:1646px;height:121px;background:#fde2c0;border:1px solid #f3c792}
.ad-secure h5{font-size:12.5px;font-weight:700;text-align:center;margin-top:8px}
.ad-secure .body{position:absolute;left:14px;top:38px;display:flex;align-items:center;gap:12px;font-size:12.5px;line-height:1.3}
.ad-help{top:1798px;height:149px;background:#e8e1f1;border:1px solid #d6cbe6;text-align:center}
.ad-help h5{color:var(--purple);font-size:21px;font-weight:400;line-height:1.1;margin-top:10px}
.ad-help p{font-size:11px;line-height:1.3;padding:4px 24px 0}
.ad-help .btn{display:inline-block;background:#333;color:var(--white);font-size:12px;font-weight:700;padding:2px 10px;margin-top:6px}

.products{left:389px;top:672px;width:680px}
.products-head{height:38px;background:var(--purple);color:var(--white);font-size:18px;font-weight:600;line-height:38px;padding-left:12px;position:relative}
.slider-arrows{position:absolute;right:10px;top:8px;display:flex;gap:14px}
.slider-arrows span{width:22px;height:22px;border-radius:50%;background:#222;display:flex;align-items:center;justify-content:center}
.product-grid{position:absolute;left:0;top:52px;width:680px;display:grid;grid-template-columns:repeat(3,213px);column-gap:21px;row-gap:26px}
.product{height:284px;border:1px solid var(--line);padding:9px 8px 0}
.product-photo{height:157px;border-radius:2px}
.price{font-size:17px;font-weight:700;color:var(--purple);margin-top:11px}
.product-name{font-size:11.5px;font-weight:600;color:var(--orange);margin-top:4px;white-space:nowrap;overflow:hidden;text-overflow:ellipsis}
.product-tag{font-size:12px;color:#222;margin-top:2px}
.product-actions{display:flex;justify-content:space-between;margin-top:10px}
.btn-cart{width:118px;height:28px;background:var(--purple);color:var(--white);font-size:12.5px;display:flex;align-items:center;justify-content:center;gap:8px}
.btn-info{width:56px;height:28px;background:var(--orange);color:var(--white);font-size:12.5px;display:flex;align-items:center;justify-content:center}

.seo-band{left:142px;top:1975px;width:916px;height:198px;background:var(--purple);color:var(--white);padding:12px 70px 0 14px}
.seo-band li{list-style:none;font-size:12.3px;line-height:1.42;display:flex;gap:22px;margin-bottom:9px}
.seo-band .bullet{margin-top:5px}

.footer-card{left:142px;top:2209px;width:916px;height:326px;background:var(--white);box-shadow:0 0 8px rgba(0,0,0,.35)}
.delivery{position:absolute;left:18px;top:24px;width:520px}
.delivery h2{font-size:22px;font-weight:400;color:var(--purple);line-height:1.2;display:flex;gap:12px;padding-left:12px}
.delivery h2 .bullet{margin-top:8px}
.delivery ul{list-style:none;margin:14px 0 14px 36px}
.delivery li{font-size:11.5px;line-height:1.6}
.footer-side{position:absolute;left:595px;top:24px;width:290px}
.footer-side h3{font-size:20px;font-weight:400;color:var(--purple)}
.footer-side p{font-size:11.5px;margin-top:1px}
.newsletter{display:flex;gap:5px;margin-top:12px;margin-bottom:22px}
.newsletter .field{width:206px;height:26px;border:1px solid #ddd;background:#f7f7f7;font-size:10px;color:#aaa;padding:6px 8px}
.newsletter .go{width:42px;height:26px;background:var(--purple);color:var(--white);font-weight:700;font-size:13px;text-align:center;line-height:26px}
.cards{display:flex;gap:6px;margin:12px 0 22px}
.cards span{width:40px;height:26px;border-radius:3px;border:1px solid #ccc}
.social{display:flex;gap:12px;margin-top:12px}
.social span{width:20px;height:20px;border-radius:50%;background:#888}

.bottom-bar{left:0;top:2605px;width:1200px;height:50px;background:var(--purple);color:var(--white);font-size:11px;display:flex;align-items:center;justify-content:center;gap:14px}
</style>
</head>
<body>

<header class="site-header abs">
  <div class="brand abs"><span class="brand-mark"></span><span class="brand-name">Parcelnook.com.au</span></div>
  <div class="phone abs">
    <svg width="20" height="20" viewBox="0 0 24 24"><path fill="#6b449b" d="M6.6 10.8a15 15 0 0 0 6.6 6.6l2.2-2.2c.3-.3.7-.4 1-.2 1.1.4 2.3.6 3.6.6.6 0 1 .4 1 1V20c0 .6-.4 1-1 1A17 17 0 0 1 3 4c0-.6.4-1 1-1h3.5c.6 0 1 .4 1 1 0 1.3.2 2.5.6 3.6.1.3 0 .7-.2 1z"/></svg>
    +61 1300 555 018
  </div>
  <div class="account-tab abs"><span>View Cart (0) / Live Help</span><span>|</span>
    <svg width="11" height="11" viewBox="0 0 12 12"><circle cx="6" cy="4" r="3" fill="#fff"/><path d="M0 12c0-4 3-5 6-5s6 1 6 5z" fill="#fff"/></svg>
    <span>LOGIN / SIGN UP</span></div>
  <div class="search abs"><span>Gift Search</span>
    <svg width="18" height="18" viewBox="0 0 20 20"><circle cx="8" cy="8" r="6" fill="none" stroke="#333" stroke-width="2"/><line x1="12.5" y1="12.5" x2="18" y2="18" stroke="#333" stroke-width="2.4"/></svg>
  </div>
</header>

<nav class="main-nav abs">
  <ul>
    <li>EASTER</li><li class="active">Mother Day</li><li>Get Well</li><li>Thank You</li><li>Birthday</li><li>Anniversary</li><li>Romance</li><li>New Baby</li><li>Childrens</li><li>For Him</li><li>For Her</li>
  </ul>
</nav>

<section class="hero abs">
  <div class="hero-photo big" role="img" aria-label="Chocolate bouquet in a green gift box, large round view"></div>
  <div class="hero-photo small" role="img" aria-label="Chocolate bouquet in a green gift box, small round view"></div>
  <div class="hero-title">
    <div class="deal">UPTO 25% OFF</div>
    <div class="product">Cocoa Cascade Chocolate Bouquet</div>
  </div>
  <div class="hero-note">Now Available with heaps of<br>Optional Add-on!</div>
  <div class="hero-tabs">
    <div>Our Classic, Cute &amp; Collection<small>Teddies &amp; Soft Toys</small></div>
    <div class="current">Upto 25% Off<small>Cocoa Cascade Chocolate Bouquet</small></div>
    <div>Australia Wide Delivery<small>Orchard Harvest</small></div>
  </div>
</section>

<aside class="promo-exclusive abs">
  <div class="promo-card orange">
    <h3>Parcelnook Exclusive</h3>
    <p>Browse through an exclusive range<br>of products on Parcelnook.</p>
    <div class="promo-label"><span class="mark"></span><span>Parcelnook.com.au</span></div>
    <span class="shop-now">Shop Now ▸</span>
  </div>
  <div class="promo-card grey">
    <h3 style="color:#222">Exclusive on Parcelnook</h3>
    <div class="promo-round" role="img" aria-label="Round chocolate praline bouquet"></div>
    <span class="shop-now">Shop Now ▸</span>
  </div>
</aside>

<section class="intro abs">
  <h1>Gift Baskets &amp; Hampers Delivered throughout Australia.</h1>
  <p class="lead">Gift Baskets and Hampers great range is now available with Gift Delivery Australia Wide! Send a gift Australia wide today. Fast delivery</p>
  <p>Gift baskets delivered Australia wide! Gift ideas for Christmas, Mother's day, birthdays, new babies and more. Gourmet gift baskets and hampers<br>including wine, fruit, teddies and more, perfect for any occasion available online!</p>
</section>

<div class="side-box abs" style="top:672px">
  <h4>Shop By Basket Price</h4>
  <ul>
    <li><span class="bullet"></span>Gifts Under $50</li>
    <li><span class="bullet"></span>Gifts $50 to $75</li>
    <li><span class="bullet"></span>Gifts $75 to $100</li>
    <li><span class="bullet"></span>Gifts $100 to $150</li>
    <li><span class="bullet"></span>Gifts Over $150</li>
  </ul>
</div>
<div class="side-box abs" style="top:899px">
  <h4>Shop By Basket Style</h4>
  <ul>
    <li><span class="bullet"></span>Chocolate Bouquets</li>
    <li><span class="bullet"></span>Plant Gifts</li>
    <li><span class="bullet"></span>Fruit Hampers</li>
    <li><span class="bullet"></span>Pamper Packs</li>
    <li><span class="bullet"></span>Lollies &amp; Sweets</li>
    <li><span class="bullet"></span>Teddy Bears &amp; Toys</li>
    <li><span class="bullet"></span>Gourmet Hampers</li>
    <li><span class="bullet"></span>Champagne &amp; Liquor</li>
    <li><span class="bullet"></span>Personalised Items</li>
    <li><span class="bullet"></span>Corporate Gifts</li>
  </ul>
</div>
<div class="side-box abs" style="top:1278px">
  <h4>Shop By Basket Occasions</h4>
  <ul>
    <li><span class="bullet"></span>Easter Gifts</li>
    <li><span class="bullet"></span>Mothers Day Gifts</li>
    <li><span class="bullet"></span>Fathers Day Gifts</li>
    <li><span class="bullet"></span>Christmas Gifts</li>
    <li><span class="bullet"></span>Valentines Day Gifts</li>
  </ul>
</div>

<div class="side-ad ad-floral abs">
  <div class="text">Get<br><b>30%</b><br>Off</div>
  <div class="flowers" role="img" aria-label="Pink floral arrangement"></div>
  <div class="caption">FLORAL ARRANGMENTS</div>
</div>
<div class="side-ad ad-secure abs">
  <h5>Payment Gateway Secured With</h5>
  <div class="body">
    <svg width="34" height="34" viewBox="0 0 34 34"><circle cx="17" cy="17" r="15" fill="none" stroke="#333" stroke-width="2"/><path d="M9 17l6 6 11-13" fill="none" stroke="#c0272d" stroke-width="3"/></svg>
    <span style="text-align:center">256 Bit<br>SSL<br>Encryption<br>Techonology</span>
    <svg width="44" height="52" viewBox="0 0 44 52"><path d="M10 24V15a12 12 0 0 1 24 0v9" fill="none" stroke="#9a9a9a" stroke-width="5"/><rect x="4" y="23" width="36" height="27" rx="3" fill="#f2b51f"/></svg>
  </div>
</div>
<div class="side-ad ad-help abs">
  <h5>Live Help<br>Support &amp; Services</h5>
  <p>For assistance with the checkout process, or speak to a member of the customer support team, Simply</p>
  <span class="btn">Click Here</span>
</div>

<main class="products abs">
  <div class="products-head">Todays Top Products
    <div class="slider-arrows">
      <span><svg width="8" height="10" viewBox="0 0 8 10"><path d="M7 0L0 5l7 5z" fill="#fff"/></svg></span>
      <span><svg width="8" height="10" viewBox="0 0 8 10"><path d="M1 0l7 5-7 5z" fill="#fff"/></svg></span>
    </div>
  </div>
  <div class="product-grid">
    <article class="product"><div class="product-photo" role="img" aria-label="Stacked white gift boxes with purple ribbon and chocolates" style="background:linear-gradient(160deg,#f5f3f7,#d9cfe6 55%,#efefef)"></div><div class="price">$54.95</div><div class="product-name">Stack Of Sweetness</div><div class="product-tag">Gift ideas Australia</div><div class="product-actions"><span class="btn-cart"><svg width="16" height="14" viewBox="0 0 16 14"><path d="M0 1h3l2 8h8l2-6H4" fill="none" stroke="#fff" stroke-width="1.6"/><circle cx="6" cy="12" r="1.4" fill="#fff"/><circle cx="12" cy="12" r="1.4" fill="#fff"/></svg>Add to Cart</span><span class="btn-info">Info ››</span></div></article>
    <article class="product"><div class="product-photo" role="img" aria-label="Colourful chocolate bouquet in a green box" style="background:radial-gradient(circle at 50% 40%,#e84a3a,#f2b43a 35%,#4b8fd6 55%,#7fc24a 75%,#f5f5f5)"></div><div class="price">$79.00</div><div class="product-name">Cocoa Cascade Chocolate Bouquet</div><div class="product-tag">Gift Basket Ideas</div><div class="product-actions"><span class="btn-cart"><svg width="16" height="14" viewBox="0 0 16 14"><path d="M0 1h3l2 8h8l2-6H4" fill="none" stroke="#fff" stroke-width="1.6"/><circle cx="6" cy="12" r="1.4" fill="#fff"/><circle cx="12" cy="12" r="1.4" fill="#fff"/></svg>Add to Cart</span><span class="btn-info">Info ››</span></div></article>
    <article class="product"><div class="product-photo" role="img" aria-label="Two wine bottles in a wooden crate with treats" style="background:linear-gradient(180deg,#f4f1ec,#c9a97a 60%,#a8855a)"></div><div class="price">$39.00</div><div class="product-name">Hillside Chardonnay &amp; Shiraz..</div><div class="product-tag">Gift Basket Ideas</div><div class="product-actions"><span class="btn-cart"><svg width="16" height="14" viewBox="0 0 16 14"><path d="M0 1h3l2 8h8l2-6H4" fill="none" stroke="#fff" stroke-width="1.6"/><circle cx="6" cy="12" r="1.4" fill="#fff"/><circle cx="12" cy="12" r="1.4" fill="#fff"/></svg>Add to Cart</span><span class="btn-info">Info ››</span></div></article>

    <article class="product"><div class="product-photo" role="img" aria-label="Basket of mixed fresh fruit" style="background:radial-gradient(circle at 50% 45%,#c8342c,#e9a23a 35%,#7a9a3a 60%,#f2f2f2 80%)"></div><div class="price">$70.00</div><div class="product-name">Orchard Harvest</div><div class="product-tag">Gift ideas Australia</div><div class="product-actions"><span class="btn-cart"><svg width="16" height="14" viewBox="0 0 16 14"><path d="M0 1h3l2 8h8l2-6H4" fill="none" stroke="#fff" stroke-width="1.6"/><circle cx="6" cy="12" r="1.4" fill="#fff"/><circle cx="12" cy="12" r="1.4" fill="#fff"/></svg>Add to Cart</span><span class="btn-info">Info ››</span></div></article>
    <article class="product"><div class="product-photo" role="img" aria-label="Wooden gift chest with wine and cheese" style="background:linear-gradient(170deg,#f6f4f2,#5b3a7e 45%,#c9a97a 75%,#f0eee9)"></div><div class="price">$89.95</div><div class="product-name">Vine And Brie Gift Chest</div><div class="product-tag">Buy Gifts Online</div><div class="product-actions"><span class="btn-cart"><svg width="16" height="14" viewBox="0 0 16 14"><path d="M0 1h3l2 8h8l2-6H4" fill="none" stroke="#fff" stroke-width="1.6"/><circle cx="6" cy="12" r="1.4" fill="#fff"/><circle cx="12" cy="12" r="1.4" fill="#fff"/></svg>Add to Cart</span><span class="btn-info">Info ››</span></div></article>
    <article class="product"><div class="product-photo" role="img" aria-label="Stacked white gift boxes with orange ribbon" style="background:linear-gradient(160deg,#f7f4f0,#f5c58a 55%,#f2f0ee)"></div><div class="price">$64.95</div><div class="product-name">Stack Of Delights</div><div class="product-tag">Send a gift Basket</div><div class="product-actions"><span class="btn-cart"><svg width="16" height="14" viewBox="0 0 16 14"><path d="M0 1h3l2 8h8l2-6H4" fill="none" stroke="#fff" stroke-width="1.6"/><circle cx="6" cy="12" r="1.4" fill="#fff"/><circle cx="12" cy="12" r="1.4" fill="#fff"/></svg>Add to Cart</span><span class="btn-info">Info ››</span></div></article>

    <article class="product"><div class="product-photo" role="img" aria-label="Tall tropical fruit arrangement" style="background:radial-gradient(ellipse at 50% 50%,#e5672a,#f0b43c 30%,#5f8f38 55%,#f3f3f3 78%)"></div><div class="price">$105.00</div><div class="product-name">The Island Breeze</div><div class="product-tag">Gift Basket Ideas</div><div class="product-actions"><span class="btn-cart"><svg width="16" height="14" viewBox="0 0 16 14"><path d="M0 1h3l2 8h8l2-6H4" fill="none" stroke="#fff" stroke-width="1.6"/><circle cx="6" cy="12" r="1.4" fill="#fff"/><circle cx="12" cy="12" r="1.4" fill="#fff"/></svg>Add to Cart</span><span class="btn-info">Info ››</span></div></article>
    <article class="product"><div class="product-photo" role="img" aria-label="Two wine bottles in a wooden crate" style="background:linear-gradient(180deg,#f4f1ec,#c4a274 60%,#9f7d52)"></div><div class="price">$39.00</div><div class="product-name">Hillside Savignon Blanc &amp; Merlot..</div><div class="product-tag">Buy Gifts Online</div><div class="product-actions"><span class="btn-cart"><svg width="16" height="14" viewBox="0 0 16 14"><path d="M0 1h3l2 8h8l2-6H4" fill="none" stroke="#fff" stroke-width="1.6"/><circle cx="6" cy="12" r="1.4" fill="#fff"/><circle cx="12" cy="12" r="1.4" fill="#fff"/></svg>Add to Cart</span><span class="btn-info">Info ››</span></div></article>
    <article class="product"><div class="product-photo" role="img" aria-label="Gold wrapped praline bouquet with purple wrap" style="background:radial-gradient(circle at 50% 42%,#7a5522,#c9a14a 35%,#6b449b 65%,#f3f3f3 82%)"></div><div class="price">$69.00</div><div class="product-name">Hazelnut Praline Bouquet</div><div class="product-tag">Gift Basket Ideas</div><div class="product-actions"><span class="btn-cart"><svg width="16" height="14" viewBox="0 0 16 14"><path d="M0 1h3l2 8h8l2-6H4" fill="none" stroke="#fff" stroke-width="1.6"/><circle cx="6" cy="12" r="1.4" fill="#fff"/><circle cx="12" cy="12" r="1.4" fill="#fff"/></svg>Add to Cart</span><span class="btn-info">Info ››</span></div></article>

    <article class="product"><div class="product-photo" role="img" aria-label="Liqueur gift set in a kraft box with glasses" style="background:linear-gradient(180deg,#f3f0ec,#8c6a45 45%,#c7a77c 75%,#efece7)"></div><div class="price">$89.00</div><div class="product-name">Velvet Irish Cream Gift Set</div><div class="product-tag">Australia wide delivery</div><div class="product-actions"><span class="btn-cart"><svg width="16" height="14" viewBox="0 0 16 14"><path d="M0 1h3l2 8h8l2-6H4" fill="none" stroke="#fff" stroke-width="1.6"/><circle cx="6" cy="12" r="1.4" fill="#fff"/><circle cx="12" cy="12" r="1.4" fill="#fff"/></svg>Add to Cart</span><span class="btn-info">Info ››</span></div></article>
    <article class="product"><div class="product-photo" role="img" aria-label="Port gift set in a kraft box with glasses" style="background:linear-gradient(180deg,#f3f0ec,#6e3a2a 45%,#c7a77c 75%,#efece7)"></div><div class="price">$69.00</div><div class="product-name">Redgum Club Tawny Port Gift Set</div><div class="product-tag">Australia wide delivery</div><div class="product-actions"><span class="btn-cart"><svg width="16" height="14" viewBox="0 0 16 14"><path d="M0 1h3l2 8h8l2-6H4" fill="none" stroke="#fff" stroke-width="1.6"/><circle cx="6" cy="12" r="1.4" fill="#fff"/><circle cx="12" cy="12" r="1.4" fill="#fff"/></svg>Add to Cart</span><span class="btn-info">Info ››</span></div></article>
    <article class="product"><div class="product-photo" role="img" aria-label="Chocolate bouquet in a purple box" style="background:radial-gradient(circle at 50% 42%,#2f5fb5,#e5a33a 30%,#d8432f 50%,#6b449b 68%,#f3f3f3 84%)"></div><div class="price">$62.00</div><div class="product-name">Sweet Medley Chocolate Box</div><div class="product-tag">Australia wide delivery</div><div class="product-actions"><span class="btn-cart"><svg width="16" height="14" viewBox="0 0 16 14"><path d="M0 1h3l2 8h8l2-6H4" fill="none" stroke="#fff" stroke-width="1.6"/><circle cx="6" cy="12" r="1.4" fill="#fff"/><circle cx="12" cy="12" r="1.4" fill="#fff"/></svg>Add to Cart</span><span class="btn-info">Info ››</span></div></article>
  </div>
</main>

<section class="seo-band abs">
  <ul>
    <li><span class="bullet"></span><span>Send Gifts to Sydney NSW, Brisbane QLD, Melbourne VIC, Canberra ACT, Adelaide SA, Perth WA, Darwin NT, Hobart TAS and more via our online store, providing our customers with Gift Baskets and Hampers Australia Wide.</span></li>
    <li><span class="bullet"></span><span>Searching for that Perfect Gift? We provide a great range in our online gift shop! As Australia's premier Gift Basket and Hamper network we can offer you an enormous and exclusive range of special gifts sent at great prices.</span></li>
    <li><span class="bullet"></span><span>We deliver all sorts of gifts including Gourmet Hampers, Fruit Baskets, Delicious Cakes, Live Plants, Herbs and Flowers, Cuddly Teddies in all shapes and sizes, Lollies, Chocolate and presents for all occasions, such as birthdays, anniversaries and even special holiday seasons throughout the year.</span></li>
    <li><span class="bullet"></span><span>All our gifts can be ordered online 24 hours a day for Delivery Australia wide. So, when it comes to buying and sending gifts online, you can rely on the experts at parcelnook.com.au!</span></li>
  </ul>
</section>

<footer class="footer-card abs">
  <div class="delivery">
    <h2><span class="bullet"></span><span>Gift Baskets &amp; Hampers Delivered<br>Throughout Australia</span></h2>
    <ul>
      <li>Browse Victorian Delivery areas including Gifts to Melbourne</li>
      <li>Find Queensland Delivery locations and Gifts to Brisbane</li>
      <li>Explore New South Wales Delivery areas with Gifts to Sydney</li>
      <li>Discover Tasmanian Delivery locations including Gifts to Hobart</li>
    </ul>
    <h2><span class="bullet"></span><span>More Australian Gift Basket &amp; Hamper<br>Delivery Locations</span></h2>
    <ul>
      <li>Find South Australian Delivery suburbs and Gifts to Adelaide</li>
      <li>Browse ACT Delivery suburbs and Gifts to Canberra</li>
      <li>Discover Northern Territory Delivery areas with Gifts to Darwin</li>
      <li>Explore Western Australia Delivery suburbs plus Gifts to Perth</li>
    </ul>
  </div>
  <div class="footer-side">
    <h3>Newsletter Signup</h3>
    <p>Keep up to date with our latest Offers</p>
    <div class="newsletter"><span class="field">Email Address</span><span class="go">GO</span></div>
    <h3>Payment Methods</h3>
    <p>Shop securely and with confidence.</p>
    <div class="cards"><span style="background:#e8eef6"></span><span style="background:#e9edf7"></span><span style="background:#dfe6f2"></span><span style="background:#fbe7d6"></span><span style="background:#e3ebf6"></span></div>
    <h3>Follow Us</h3>
    <p style="color:var(--purple)">Keep up with everything Hiking!</p>
    <div class="social"><span></span><span></span><span></span><span></span></div>
  </div>
</footer>

<div class="bottom-bar abs">
  <span>Home</span><span>|</span><span>About Us</span><span>|</span><span>Links</span><span>|</span><span>Search Site</span><span>|</span><span>Contact Us</span><span style="margin-left:10px">Terms and Conditions</span><span>|</span><span>Privacy Policy</span><span>|</span><span>© Copyright 2014 Parcelnook.</span>
</div>

</body>
</html>
```